BANNER AD FOR RUGBY LEAGUE REUINION

MUST BE 605X303 – jpeg format AND 233X233 – jpeg format

(SOME IDEAS - A FOOTBALL FIELD??? A MAGPIE KICKING A GOAL??)

MAGPIE IN PICTURE DOESNT HAVE TO BE USED, IT WAS JUST PUT THERE AS AN IDEA

Target Market(s)

rugby league supporters

Font styles to use
Serif
Sans Serif

Colors

Designer to choose colors to be used in the design.

Requirements
Must have
• MUST HAVE MAGPIE SOMEWHERE ON DESIGN
MUST SAY "RETURN TO CAMPBELLTOWN"
MUST HAVE 12TH JULY AT 7PM
Nice to have
• FOOTBALL OVAL GRASS

```html
<!DOCTYPE html>
<html lang="en">
<head>
<meta charset="utf-8">
<title>Return to Campbelltown – Rugby League Reunion</title>
<link href="https://fonts.googleapis.com/css2?family=Lato:wght@300;400&display=swap" rel="stylesheet">
<style>
  :root {
    --sky: #9c8fb0;
    --stand-light: #6f7a78;
    --stand-dark: #3d4a46;
    --grass-far: #3c8f35;
    --grass-near: #5fbf3e;
    --ink: #ffffff;
    --seam: #3f6f4a;
  }
  html, body {
    margin: 0;
    padding: 0;
    width: 1200px;
    height: 601px;
    overflow: hidden;
    background: #2f3a36;
  }
  .banner {
    position: relative;
    width: 1200px;
    height: 601px;
    overflow: hidden;
    font-family: "Lato", "Helvetica Neue", Arial, sans-serif;
    color: var(--ink);
  }
  .stadium-backdrop {
    position: absolute;
    inset: 0;
    background:
      radial-gradient(ellipse 70% 30% at 60% 58%, rgba(120, 200, 80, 0.35), transparent 70%),
      linear-gradient(180deg,
        var(--sky) 0%,
        #7d7a8e 7%,
        var(--stand-light) 14%,
        var(--stand-dark) 30%,
        #55625c 40%,
        var(--grass-far) 48%,
        #4aa83a 68%,
        var(--grass-near) 100%);
  }
  .stadium-backdrop::after {
    content: "";
    position: absolute;
    inset: 0;
    background: rgba(20, 30, 25, 0.12);
  }
  .mascot-spot {
    position: absolute;
    left: 1036px;
    top: 4px;
    width: 156px;
    height: 156px;
    border-radius: 50%;
    background: radial-gradient(circle, rgba(235, 235, 240, 0.55), rgba(235, 235, 240, 0) 70%);
  }
  .balls {
    position: absolute;
    left: 330px;
    top: 90px;
    width: 540px;
    height: 170px;
  }
  .rule {
    position: absolute;
    left: 307px;
    width: 588px;
    height: 2px;
    background: rgba(255, 255, 255, 0.85);
  }
  .rule--top { top: 288px; }
  .rule--bottom { top: 516px; }
  .kicker {
    position: absolute;
    left: 307px;
    top: 296px;
    width: 588px;
    margin: 0;
    display: flex;
    justify-content: space-between;
    font-weight: 300;
    font-size: 40px;
    line-height: 48px;
  }
  .headline {
    position: absolute;
    left: 300px;
    top: 345px;
    width: 600px;
    margin: 0;
    text-align: center;
    font-weight: 400;
    font-size: 66px;
    line-height: 72px;
    letter-spacing: 0.5px;
  }
  .event-time {
    position: absolute;
    left: 300px;
    top: 432px;
    width: 600px;
    margin: 0;
    display: flex;
    justify-content: center;
    align-items: center;
    gap: 14px;
    font-weight: 300;
    font-size: 36px;
    line-height: 44px;
  }
  .event-time sup {
    font-size: 18px;
    vertical-align: 16px;
    margin-left: 2px;
  }
  .event-time .clock {
    width: 36px;
    height: 36px;
  }
</style>
</head>
<body>
<main class="banner">
  <div class="stadium-backdrop" role="img" aria-label="Blurred photo of a floodlit football oval with green grass and grandstands at dusk"></div>
  <div class="mascot-spot" role="img" aria-label="Magpie mascot illustration"></div>

  <svg class="balls" viewBox="0 0 540 170" aria-hidden="true">
    <defs>
      <g id="ball">
        <ellipse cx="0" cy="0" rx="86" ry="56" fill="#ffffff"/>
        <path d="M-78 0 H78" stroke="var(--seam)" stroke-width="7" fill="none"/>
        <path d="M-30 -12 V12 M-10 -12 V12 M10 -12 V12 M30 -12 V12" stroke="var(--seam)" stroke-width="6"/>
        <path d="M-60 -38 Q-80 0 -60 38 M60 -38 Q80 0 60 38" stroke="var(--seam)" stroke-width="5" fill="none"/>
      </g>
    </defs>
    <use href="#ball" transform="translate(96 85) rotate(-35)"/>
    <use href="#ball" transform="translate(268 85) rotate(-35)"/>
    <use href="#ball" transform="translate(444 85) rotate(-35)"/>
  </svg>

  <div class="rule rule--top"></div>
  <p class="kicker" aria-label="Return to">
    <span>R</span><span>E</span><span>T</span><span>U</span><span>R</span><span>N</span><span>T</span><span>O</span>
  </p>
  <h1 class="headline">CAMPBELLTOWN</h1>
  <p class="event-time">
    <span>12<sup>TH</sup> JULY -</span>
    <svg class="clock" viewBox="0 0 36 36" aria-label="Time">
      <circle cx="18" cy="20" r="12" fill="none" stroke="#fff" stroke-width="3"/>
      <path d="M18 13 V20 L23 23" fill="none" stroke="#fff" stroke-width="3" stroke-linecap="round"/>
      <path d="M4 9 A7 7 0 0 1 11 3 M32 9 A7 7 0 0 0 25 3" fill="none" stroke="#fff" stroke-width="3" stroke-linecap="round"/>
      <path d="M10 31 L8 34 M26 31 L28 34" stroke="#fff" stroke-width="3" stroke-linecap="round"/>
    </svg>
    <span>7 PM</span>
  </p>
  <div class="rule rule--bottom"></div>
</main>
</body>
</html>
```